Tamarack Hearth Partners Business Card

Looking for a new business card layout. We are a real estate firm w/ a logo, old design attached. Must keep the same elements on there, just need a fresh look and possible some foil accents. Looking for a simpler design w/ more modern style.

Target Market(s)

Real Estate clients

Industry/Entity Type

Real Estate Agent

Contact Information for Business Card

see attached

Font styles to use
Sans Serif

Requirements
Must have
• all elements on current biz card
Nice to have
• modern look, simpler than we have!
Should not have
• no serif fonts

```html
<!DOCTYPE html>
<html lang="en">
<head>
<meta charset="utf-8">
<title>Tamarack Hearth Partners Business Card</title>
<link rel="stylesheet" href="https://fonts.googleapis.com/css2?family=Montserrat:wght@300;400;600&display=swap">
<style>
  :root {
    --backdrop: #e4e4e4;
    --card: #1b1b1b;
    --ribbon: #9b9b9b;
    --silver: #c8c8c8;
    --text-light: #e6e6e6;
    --text-muted: #bdbdbd;
    --photo-warm: #d9c6a4;
    --photo-deep: #8f7b63;
  }
  * { box-sizing: border-box; margin: 0; padding: 0; }
  html, body { width: 1200px; height: 800px; overflow: hidden; }
  body {
    background: var(--backdrop);
    font-family: "Montserrat", sans-serif;
    display: flex;
    flex-direction: column;
    align-items: center;
    justify-content: center;
    gap: 28px;
  }
  .card {
    position: relative;
    width: 640px;
    height: 366px;
    background: var(--card);
    border-radius: 4px;
    box-shadow: 0 6px 18px rgba(0,0,0,.22);
    overflow: hidden;
  }

  /* front */
  .ribbon {
    position: absolute;
    left: 390px; top: 112px;
    width: 250px; height: 52px;
  }
  .ribbon svg { display: block; width: 100%; height: 100%; }
  .agent-photo {
    position: absolute;
    left: 468px; top: 14px;
    width: 110px; height: 110px;
    border-radius: 50%;
    border: 3px solid #f2f2f2;
    background: radial-gradient(circle at 50% 45%, var(--photo-warm) 0%, #c6ad86 55%, var(--photo-deep) 100%);
  }
  .agent-name {
    position: absolute;
    right: 28px; top: 118px;
    text-align: right;
    color: #ffffff;
  }
  .agent-name .name {
    font-weight: 300;
    font-size: 24px;
    letter-spacing: 2px;
    line-height: 1.1;
  }
  .agent-name .title {
    font-weight: 400;
    font-size: 10px;
    letter-spacing: 1.5px;
  }
  .office {
    position: absolute;
    right: 28px; top: 182px;
    text-align: right;
    color: var(--text-light);
    font-size: 12px;
    line-height: 1.6;
  }
  .office .pin { width: 9px; height: 12px; vertical-align: -1px; margin-right: 5px; }
  .website {
    position: absolute;
    right: 28px; top: 250px;
    color: var(--text-light);
    font-size: 12px;
  }
  .brand {
    position: absolute;
    left: 32px; top: 128px;
    color: var(--text-muted);
    font-weight: 600;
    font-size: 22px;
    letter-spacing: 2px;
    line-height: 1.1;
    text-transform: uppercase;
  }
  .contacts {
    position: absolute;
    left: 32px; bottom: 26px;
    list-style: none;
    color: var(--text-light);
    font-size: 12px;
    line-height: 1.75;
  }
  .contacts svg { width: 12px; height: 12px; vertical-align: -2px; margin-right: 8px; }

  /* back */
  .card-back {
    display: flex;
    align-items: center;
    justify-content: center;
  }
  .brand-foil {
    color: var(--silver);
    font-weight: 600;
    font-size: 36px;
    letter-spacing: 3px;
    text-transform: uppercase;
    text-align: center;
    line-height: 1.15;
  }
</style>
</head>
<body>

  <section class="card card-front">
    <div class="ribbon">
      <svg viewBox="0 0 250 52" preserveAspectRatio="none">
        <polygon points="0,0 250,0 250,52 0,52 22,26" fill="var(--ribbon)"/>
      </svg>
    </div>
    <div class="agent-photo" role="img" aria-label="Portrait photo of the broker"></div>
    <div class="agent-name">
      <p class="name">MAREN ELLISON</p>
      <p class="title">PRINCIPAL BROKER</p>
    </div>
    <div class="office">
      <p><svg class="pin" viewBox="0 0 9 12"><path d="M4.5 0A4.5 4.5 0 0 0 0 4.5C0 8 4.5 12 4.5 12S9 8 9 4.5A4.5 4.5 0 0 0 4.5 0Zm0 6.2a1.7 1.7 0 1 1 0-3.4 1.7 1.7 0 0 1 0 3.4Z" fill="#bdbdbd"/></svg>482 NW Juniper Ave</p>
      <p>Bend Falls, OR 97000</p>
    </div>
    <p class="website">www.Tamarackhearth-Homes.com</p>

    <p class="brand">Tamarack Hearth<br>Partners</p>

    <ul class="contacts">
      <li><svg viewBox="0 0 12 12"><path d="M1 3.5C1 2 2 1 3.5 1h5C10 1 11 2 11 3.5v.8H8.5v-1h-5v1H1ZM2 5.2h8L11 11H1Z" fill="#bdbdbd"/></svg>555.210.3184</li>
      <li><svg viewBox="0 0 12 12"><rect x="3" y="0.5" width="6" height="11" rx="1" fill="none" stroke="#bdbdbd" stroke-width="1.2"/><circle cx="6" cy="9.6" r=".7" fill="#bdbdbd"/></svg>555.210.4479</li>
      <li><svg viewBox="0 0 12 12"><rect x="0.5" y="2.5" width="11" height="7.5" fill="#bdbdbd"/><path d="M0.5 2.5 6 7l5.5-4.5" fill="none" stroke="#1b1b1b" stroke-width="1"/></svg>maren@tamarackhearth.com</li>
    </ul>
  </section>

  <section class="card card-back">
    <p class="brand-foil">Tamarack Hearth<br>Partners</p>
  </section>

</body>
</html>
```